Designing of Orientation Materials and Innovative Ways to ‘Market’ Procurement Function

To Market and promote Procurement function and it’s ‘real’ capabilities clearly, to demonstrate that the function is an enabler instead being perceive as a barrier to other internal functions. Sometimes due to the lack of a common language even makes it difficult for other functions (e.g) Marketing and Procurement to understand each other’s aims and intentions.
The audience could be from all functions such as; Human Resource, Finance, Sales & Marketing, Supply Chain/Procurement, Corporate Affairs and Information System.

```html
<!DOCTYPE html>
<html lang="en">
<head>
<meta charset="utf-8">
<title>Market and Promote Procurement Function</title>
<link rel="stylesheet" href="https://fonts.googleapis.com/css2?family=PT+Sans:wght@400;700&family=PT+Sans+Narrow:wght@700&display=swap">
<style>
  :root {
    --paper: #efefed;
    --ink: #0d0d0d;
    --text: #1a1a1a;
    --value-cap: #3fdc94;
    --value-light: #b4fbe0;
    --value-mid: #5ff5b2;
    --value-dark: #16e05a;
    --demand-cap: #04a894;
    --demand-light: #20f4ea;
    --demand-mid: #00dcc8;
    --demand-dark: #0a9f86;
    --tco-cap: #c0520f;
    --tco-light: #f7b62e;
    --tco-mid: #ee8a14;
    --tco-dark: #c82300;
    --price-cap: #d9ab1f;
    --price-light: #fdf080;
    --price-mid: #f9e22e;
    --price-dark: #eca600;
    --supply-cap: #763a47;
    --supply-light: #e4a9b1;
    --supply-mid: #b86070;
    --supply-dark: #5a1420;
  }
  * { margin: 0; padding: 0; box-sizing: border-box; }
  html, body { width: 1200px; height: 800px; overflow: hidden; }
  body {
    background: var(--paper);
    font-family: "PT Sans", sans-serif;
    color: var(--text);
    position: relative;
  }
  .column-heading {
    position: absolute;
    top: 34px;
    font-weight: 700;
    font-size: 33px;
    color: var(--ink);
    white-space: nowrap;
  }
  .column-heading--value { left: 152px; }
  .column-heading--role { left: 782px; }
  .pyramid { position: absolute; left: 0; top: 0; }
  .tier-label {
    font-family: "PT Sans", sans-serif;
    font-weight: 700;
    font-size: 25px;
    fill: var(--ink);
    text-anchor: middle;
  }
  .note {
    position: absolute;
    font-size: 21px;
    line-height: 28px;
    white-space: nowrap;
  }
  .note--value { text-align: right; }
  .note--role { text-align: left; }
  .main-title {
    position: absolute;
    left: 0; right: 0;
    top: 716px;
    text-align: center;
    font-family: "PT Sans Narrow", sans-serif;
    font-weight: 700;
    font-size: 46px;
    letter-spacing: 0.5px;
    color: var(--ink);
  }
</style>
</head>
<body>
  <h2 class="column-heading column-heading--value">Value Proposition</h2>
  <h2 class="column-heading column-heading--role">Role of Procurement</h2>

  <svg class="pyramid" width="1200" height="800" viewBox="0 0 1200 800">
    <defs>
      <linearGradient id="grad-value" x1="0" x2="1"><stop offset="0" stop-color="var(--value-light)"/><stop offset=".5" stop-color="var(--value-mid)"/><stop offset="1" stop-color="var(--value-dark)"/></linearGradient>
      <linearGradient id="grad-demand" x1="0" x2="1"><stop offset="0" stop-color="var(--demand-light)"/><stop offset=".55" stop-color="var(--demand-mid)"/><stop offset="1" stop-color="var(--demand-dark)"/></linearGradient>
      <linearGradient id="grad-tco" x1="0" x2="1"><stop offset="0" stop-color="var(--tco-light)"/><stop offset=".5" stop-color="var(--tco-mid)"/><stop offset="1" stop-color="var(--tco-dark)"/></linearGradient>
      <linearGradient id="grad-price" x1="0" x2="1"><stop offset="0" stop-color="var(--price-light)"/><stop offset=".55" stop-color="var(--price-mid)"/><stop offset="1" stop-color="var(--price-dark)"/></linearGradient>
      <linearGradient id="grad-supply" x1="0" x2="1"><stop offset="0" stop-color="var(--supply-light)"/><stop offset=".5" stop-color="var(--supply-mid)"/><stop offset="1" stop-color="var(--supply-dark)"/></linearGradient>
      <filter id="base-shadow" x="-10%" y="-50%" width="120%" height="200%"><feGaussianBlur stdDeviation="4"/></filter>
    </defs>

    <ellipse cx="610" cy="666" rx="300" ry="6" fill="#8a8a8a" opacity=".55" filter="url(#base-shadow)"/>

    <!-- Supply Assurance -->
    <polygon points="363,537 857,537 900,570 321,570" fill="var(--supply-cap)"/>
    <rect x="321" y="570" width="579" height="90" fill="url(#grad-supply)"/>
    <path d="M321,600 C380,575 440,610 520,630 C600,650 700,630 800,570 L321,570 Z" fill="#fff" opacity=".12"/>
    <text class="tier-label" x="611" y="626">Supply Assurance</text>

    <!-- Price -->
    <polygon points="405,418 815,418 857,458 363,458" fill="var(--price-cap)"/>
    <rect x="363" y="458" width="494" height="79" fill="url(#grad-price)"/>
    <path d="M363,482 C420,462 480,490 560,508 C640,524 700,500 775,458 L363,458 Z" fill="#fff" opacity=".15"/>
    <text class="tier-label" x="611" y="510">Price</text>

    <!-- Total cost of Ownership -->
    <polygon points="448,298 773,298 815,338 405,338" fill="var(--tco-cap)"/>
    <rect x="405" y="338" width="410" height="80" fill="url(#grad-tco)"/>
    <path d="M405,362 C450,350 500,370 560,384 C620,396 680,375 745,338 L405,338 Z" fill="#fff" opacity=".12"/>
    <text class="tier-label" x="611" y="372">Total cost of</text>
    <text class="tier-label" x="611" y="403">Ownership</text>

    <!-- Demand Management -->
    <polygon points="490,178 730,178 773,218 448,218" fill="var(--demand-cap)"/>
    <rect x="448" y="218" width="325" height="80" fill="url(#grad-demand)"/>
    <path d="M448,245 C490,232 530,252 580,262 C630,270 670,252 718,218 L448,218 Z" fill="#fff" opacity=".12"/>
    <text class="tier-label" x="611" y="272">Demand Management</text>

    <!-- Value Management -->
    <polygon points="527,75 693,75 730,98 490,98" fill="var(--value-cap)"/>
    <rect x="490" y="98" width="240" height="80" fill="url(#grad-value)"/>
    <path d="M490,124 C520,112 550,128 590,140 C630,150 660,130 690,98 L490,98 Z" fill="#fff" opacity=".15"/>
    <text class="tier-label" x="611" y="157">Value Management</text>
  </svg>

  <p class="note note--value" style="right:780px; top:108px;">Increase business value<br>derived from spend</p>
  <p class="note note--value" style="right:823px; top:212px;">Reduce demand<br>activity,complexity &amp;<br>variablity</p>
  <p class="note note--value" style="right:865px; top:345px;">Shift from lowest<br>price to TCO</p>
  <p class="note note--value" style="right:890px; top:461px;">Right goods/services<br>at the right price</p>
  <p class="note note--value" style="right:927px; top:564px;">Right goods/services<br>at the right time &amp;<br>Place</p>

  <p class="note note--role" style="left:786px; top:105px;">Trusted business advisor<br>and change agent</p>
  <p class="note note--role" style="left:836px; top:220px;">Spend/budget consultant<br>&amp; relationship manager</p>
  <p class="note note--role" style="left:858px; top:340px;">Supply expert/Team<br>leader/project manager</p>
  <p class="note note--role" style="left:903px; top:469px;">Negotiator</p>
  <p class="note note--role" style="left:955px; top:592px;">Buyer/planner</p>

  <h1 class="main-title">MARKET AND PROMOTE PROCUREMENT FUNCTION</h1>
</body>
</html>
```